QVAR Individual and Corporate Development Business Card Design

QVAR needs a business card design that is aligned with it's values and targetted markets. Harmonic Lattice of Cognition Network's self diagnosis model and tools, which can be used for personal improvement and team/business performance enhancement, is based on the learnings of over 20 years of medical practitioning. QVAR supercharges personal effectiveness and awareness to also increase team and business performance.

The targetted markets are high performance individuals and teams who aspire seek to enhance their capabilities and achieve their absolute best potential.

Look and feel for the business card design we are looking for is high technology, premium, fresh, new and medical.

Target Market(s)

Industry/Entity Type

Business Consultant

Contact Information for Business Card

Logo, Full Name, Title, Phone number, Email, company name, Address,

Font styles to use
Sans Serif

Requirements
Must have
• Tag line: Maximising Performance for Highly Effective People
• Please use same colours as the logo.

```html
<!DOCTYPE html>
<html lang="en">
<head>
<meta charset="utf-8">
<title>QVAR Business Card</title>
<link href="https://fonts.googleapis.com/css2?family=Open+Sans:wght@400;600;700&display=swap" rel="stylesheet">
<style>
  :root {
    --backdrop: #4a423d;
    --card: #0d0d0d;
    --teal: #1fb3c8;
    --white: #f2f2f2;
    --silver: #c9c9c9;
    --divider: #3a3a3a;
  }
  * { margin: 0; padding: 0; box-sizing: border-box; }
  html, body { width: 1200px; height: 900px; overflow: hidden; }
  body {
    background: var(--backdrop);
    font-family: "Open Sans", Arial, sans-serif;
    display: flex;
    align-items: center;
    justify-content: center;
    gap: 48px;
  }
  .card {
    width: 530px;
    height: 303px;
    background: var(--card);
    position: relative;
    box-shadow: 0 10px 30px rgba(0,0,0,.45);
  }
  /* front */
  .card-front { display: flex; align-items: center; }
  .brand {
    width: 255px;
    padding-left: 38px;
    color: var(--teal);
  }
  .brand-name {
    font-weight: 700;
    font-size: 54px;
    line-height: 1;
    letter-spacing: 2px;
  }
  .brand-full {
    margin-top: 8px;
    font-weight: 600;
    font-size: 11.5px;
    line-height: 1.2;
    text-transform: uppercase;
    letter-spacing: .3px;
  }
  .divider {
    width: 1px;
    height: 200px;
    background: var(--divider);
  }
  .details {
    padding-left: 22px;
    color: var(--white);
    font-size: 14px;
    line-height: 1.35;
  }
  .person-name {
    color: var(--teal);
    font-weight: 600;
    font-size: 19px;
    letter-spacing: .5px;
    text-transform: uppercase;
  }
  .person-title { margin-bottom: 14px; }
  .address { margin-bottom: 12px; }
  .contact-list { list-style: none; }
  .contact-list li { display: flex; align-items: center; gap: 10px; }
  .contact-list svg { width: 11px; height: 11px; fill: var(--teal); flex: none; }
  /* back */
  .card-back {
    display: flex;
    flex-direction: column;
    align-items: center;
    justify-content: center;
    color: var(--silver);
    text-align: center;
  }
  .card-back .brand-name { font-size: 60px; color: var(--silver); }
  .card-back .brand-full { color: var(--silver); font-size: 12.5px; margin-top: 6px; }
  .card-back .rule { width: 250px; height: 1px; background: var(--divider); margin: 12px 0 16px; }
  .tagline {
    font-size: 13px;
    font-weight: 600;
    text-transform: uppercase;
    letter-spacing: 1px;
    line-height: 1.5;
  }
</style>
</head>
<body>
  <section class="card card-front">
    <div class="brand">
      <div class="brand-name">QVAR</div>
      <div class="brand-full">Harmonic Lattice<br>of Cognition Network</div>
    </div>
    <div class="divider"></div>
    <div class="details">
      <div class="person-name">Marcus Ellery</div>
      <div class="person-title">Managing Director</div>
      <div class="address">48 Meridian Row<br>Harbour City, 204817.</div>
      <ul class="contact-list">
        <li><svg viewBox="0 0 24 24"><path d="M6.6 10.8a15 15 0 0 0 6.6 6.6l2.2-2.2c.3-.3.7-.4 1-.2 1.1.4 2.3.6 3.6.6.6 0 1 .4 1 1V20c0 .6-.4 1-1 1A17 17 0 0 1 3 4c0-.6.4-1 1-1h3.5c.6 0 1 .4 1 1 0 1.3.2 2.5.6 3.6.1.3 0 .7-.2 1z"/></svg>000-555 010 203</li>
        <li><svg viewBox="0 0 24 24"><path d="M2 5h20v14H2z M2 5l10 8 10-8" fill="none" stroke="currentColor"/><path d="M2 5h20v2l-10 7L2 7z M2 9l10 7 10-7v10H2z"/></svg>info@qvarmail.com</li>
        <li><svg viewBox="0 0 24 24"><path d="M10 14a4 4 0 0 0 5.7 0l4-4a4 4 0 0 0-5.7-5.7l-1.5 1.5 1.4 1.4 1.5-1.5a2 2 0 0 1 2.9 2.9l-4 4a2 2 0 0 1-2.9 0zM14 10a4 4 0 0 0-5.7 0l-4 4a4 4 0 0 0 5.7 5.7l1.5-1.5-1.4-1.4-1.5 1.5a2 2 0 0 1-2.9-2.9l4-4a2 2 0 0 1 2.9 0z"/></svg>www.qvarnetwork.com</li>
      </ul>
    </div>
  </section>

  <section class="card card-back">
    <div class="brand-name">QVAR</div>
    <div class="brand-full">Harmonic Lattice of Cognition Network</div>
    <div class="rule"></div>
    <p class="tagline">Maximising Performance for<br>Highly Effective People</p>
  </section>
</body>
</html>
```